New business card for my lawn and landscape business

Dorrin Yard and Building is a full-service lawn care, landscaping, and light construction company serving Paragould and the Northeast Arkansas region. The business is owned and operated by Marcus Toller, with a reputation for hands-on, detail-oriented service, dependable crews, and quality results for both residential and commercial clients. A well regarded business with great reviews.
Owner Marcus Toller
Dorrinyardandbuilding.example

Target Market(s)

Commercial, Middle, and upper class in north east Arkansas

Industry/Entity Type

Lawn maintenance and landscape

Contact Information for Business Card

Dorrin Yard And Building Professional lawn care, landscaping, and property improvement in Northeast Arkansas. • lawn maintenance •lawn treatments and weed control • exterior projects • Custom landscape design & installation • Sod, trees, rock & drainage solutions • Residential & commercial services Reliable. Detailed. Done right.

Requirements
Must have
• Business name, service area, list of some of our services, clean design that represents
Nice to have
• Unique. Different design element than just grass because its already in n the logo. Picture of a warm season (south) lawn or landscape. Pictures of the type of work we do

```html
<!DOCTYPE html>
<html lang="en">
<head>
<meta charset="utf-8">
<title>Dorrin Yard and Building – Business Card</title>
<link href="https://fonts.googleapis.com/css2?family=Poppins:wght@300;400;500;600;700&display=swap" rel="stylesheet">
<style>
  :root {
    --page-bg: #e7e8ea;
    --card-black: #050608;
    --brand-green: #6fb23f;
    --text-white: #ffffff;
    --text-soft: #e4e6e3;
    --rule-grey: #b9bbbd;
  }
  * { margin: 0; padding: 0; box-sizing: border-box; }
  html, body {
    width: 1195px; height: 1200px; overflow: hidden;
    background: var(--page-bg);
    font-family: 'Poppins', sans-serif;
  }
  .card {
    position: absolute;
    width: 579px; height: 331px;
    overflow: hidden;
  }
  .card--front { left: 307px; top: 188px; background: var(--card-black); }
  .card--back { left: 313px; top: 680px; }

  .card-band { position: absolute; left: 0; bottom: 0; width: 579px; height: 19px; }

  .brand {
    position: absolute;
    display: flex; align-items: center; gap: 10px;
  }
  .brand-dot {
    width: 26px; height: 26px; border-radius: 50%;
    background: var(--brand-green); flex: none;
  }
  .brand-name {
    font-weight: 600; font-size: 21px; line-height: 1.15;
    color: var(--brand-green);
    width: 160px;
  }
  .card--front .brand { left: 36px; top: 126px; }

  .owner { position: absolute; right: 34px; top: 26px; text-align: right; }
  .owner-name { font-weight: 600; font-size: 24px; color: var(--brand-green); letter-spacing: 1px; line-height: 1.2; }
  .owner-role { font-weight: 600; font-size: 14px; color: var(--text-white); letter-spacing: 1px; }

  .contact-list { position: absolute; right: 34px; top: 118px; list-style: none; }
  .contact-item {
    display: flex; align-items: center; justify-content: flex-end; gap: 10px;
    height: 21px; font-size: 10px; color: var(--text-white); letter-spacing: .5px;
  }
  .contact-icon { width: 14px; height: 14px; flex: none; }

  .divider { position: absolute; left: 326px; top: 190px; width: 219px; height: 1px; background: var(--rule-grey); }

  .areas-title {
    position: absolute; right: 34px; top: 199px;
    font-weight: 500; font-size: 14px; color: var(--brand-green); letter-spacing: .8px;
  }
  .areas {
    position: absolute; left: 328px; top: 227px; width: 217px;
    display: grid; grid-template-columns: 1fr auto; row-gap: 8px;
    list-style: none;
  }
  .area { font-size: 9.5px; color: var(--text-white); letter-spacing: .5px; display: flex; align-items: center; gap: 5px; }
  .area::before { content: ""; width: 6px; height: 6px; border-radius: 50%; background: var(--brand-green); }
  .area:nth-child(even) { justify-content: flex-end; }
  .region {
    position: absolute; left: 328px; top: 276px; width: 219px;
    font-size: 11px; color: var(--brand-green); letter-spacing: 2.3px;
    white-space: nowrap;
  }

  .back-photo {
    position: absolute; inset: 0;
    background: linear-gradient(180deg, #4e5a62 0%, #55606a 22%, #5d5048 42%, #3c4636 60%, #324c2c 80%, #2f4a2a 100%);
  }
  .card--back .brand { left: 205px; top: 86px; }
  .card--back .brand-name { color: var(--text-white); }
  .card--back .brand-dot { background: var(--text-white); }

  .services {
    position: absolute; top: 214px; left: 32px; right: 29px;
    display: flex; justify-content: space-between;
  }
  .service-col {
    font-weight: 300; font-size: 10.3px; line-height: 13px;
    color: var(--text-soft); letter-spacing: -.15px;
  }
  .service-col:nth-child(1) { width: 142px; text-align: justify; }
  .service-col:nth-child(3) { width: 152px; }
  .service-col:nth-child(5) { width: 147px; }
  .service-rule { width: 1px; height: 62px; background: var(--rule-grey); margin-top: 2px; }
  .bullet { display: inline-block; width: 7px; height: 7px; border-radius: 50%; background: var(--brand-green); margin-right: 5px; vertical-align: 0; }
</style>
</head>
<body>

<section class="card card--front">
  <div class="brand">
    <span class="brand-dot"></span>
    <span class="brand-name">Dorrin Yard and Building</span>
  </div>

  <div class="owner">
    <div class="owner-name">Marcus Toller</div>
    <div class="owner-role">Owner</div>
  </div>

  <ul class="contact-list">
    <li class="contact-item">(555) 014-2286
      <svg class="contact-icon" viewBox="0 0 14 14"><circle cx="7" cy="7" r="6.3" fill="none" stroke="#6fb23f" stroke-width="1"/><path d="M4.6 4.2l1.2-.4.8 1.6-.7.6c.4.9 1 1.5 1.9 1.9l.6-.7 1.6.8-.4 1.2c-2.6.2-5.2-2.4-5-5z" fill="#6fb23f"/></svg>
    </li>
    <li class="contact-item">Harlow Creek, AR 72999
      <svg class="contact-icon" viewBox="0 0 14 14"><circle cx="7" cy="7" r="6.3" fill="none" stroke="#6fb23f" stroke-width="1"/><path d="M7 3.2a2.5 2.5 0 0 1 2.5 2.5c0 1.8-2.5 4.6-2.5 4.6S4.5 7.5 4.5 5.7A2.5 2.5 0 0 1 7 3.2z" fill="#6fb23f"/><circle cx="7" cy="5.7" r="1" fill="#050608"/></svg>
    </li>
    <li class="contact-item">www.dorrinyardandbuilding.example
      <svg class="contact-icon" viewBox="0 0 14 14" fill="none" stroke="#6fb23f" stroke-width=".8"><circle cx="7" cy="7" r="6.3"/><ellipse cx="7" cy="7" rx="2.6" ry="6.3"/><path d="M.7 7h12.6M1.8 4h10.4M1.8 10h10.4"/></svg>
    </li>
  </ul>

  <div class="divider"></div>
  <h2 class="areas-title">Locations Served</h2>
  <ul class="areas">
    <li class="area">Brookland, AR</li>
    <li class="area">Jonesboro, AR</li>
    <li class="area">Paragould, AR</li>
    <li class="area">Walnut Ridge, AR</li>
  </ul>
  <p class="region">Serving Northeast Arkansas</p>

  <svg class="card-band" viewBox="0 0 579 19" preserveAspectRatio="none">
    <defs><linearGradient id="bandFront" x1="0" x2="1"><stop offset="0" stop-color="#f1f1f1"/><stop offset=".45" stop-color="#c9cacc"/><stop offset="1" stop-color="#6d6e70"/></linearGradient></defs>
    <rect width="579" height="19" fill="url(#bandFront)"/>
    <path d="M0 0H330L318 12H0z" fill="#f7f7f7"/>
    <path d="M0 8H318L312 12H0z" fill="#050608"/>
  </svg>
</section>

<section class="card card--back">
  <div class="back-photo" role="img" aria-label="Photo of a freshly mowed suburban lawn with a work truck and trailer in front of brick houses"></div>

  <div class="brand">
    <span class="brand-dot"></span>
    <span class="brand-name">Dorrin Yard and Building</span>
  </div>

  <div class="services">
    <p class="service-col"><span class="bullet"></span>Dorrin Yard And Building Professional lawn care, landscaping, and property improvement in Northeast Arkansas</p>
    <span class="service-rule"></span>
    <p class="service-col"><span class="bullet"></span>Lawn maintenance, lawn treatments and weed control<br><span class="bullet"></span>Exterior projects.<br><span class="bullet"></span>Custom landscape design &amp; installation</p>
    <span class="service-rule"></span>
    <p class="service-col"><span class="bullet"></span>Sod, trees, rock &amp; drainage solutions<br><span class="bullet"></span>Residential &amp; commercial services Reliable. Detailed. Done right</p>
  </div>

  <svg class="card-band" viewBox="0 0 579 19" preserveAspectRatio="none">
    <defs><linearGradient id="bandBack" x1="0" x2="1"><stop offset="0" stop-color="#f1f1f1"/><stop offset=".45" stop-color="#c9cacc"/><stop offset="1" stop-color="#6d6e70"/></linearGradient></defs>
    <rect width="579" height="19" fill="url(#bandBack)"/>
    <path d="M0 0H330L318 12H0z" fill="#f7f7f7"/>
    <path d="M0 8H318L312 12H0z" fill="#2f4a2a"/>
  </svg>
</section>

</body>
</html>
```